Photoshop Design Project

Just looking to use some existing element in emails and printed flyers for a lunch menu promo.

I am attaching a menu in progress to reference only the front page design of a chalkboard, chalk fonts, tagline of :Break from the Status Quo for Lunch On The GO. Its on the front of the menu.

I just want to drop in a photo of each on three separate pieces with description.

THe design should not be a match to the front of the menu, just utilize its elements. the design is not a lead at all, these should remain familiar with the front of the menu, but please use the elements to your design preference.

Ok to submit one layout that we can repeat, or ok to submit three different versions

Must stick with the colors though, they are brand color combo, not exact by color code, but the oranges and the browns need to stay somewhere and in some capacity.
SO menu attached, check out the front cover for inspirations, to go in email sends embedded, and to print as a flyer.

There are also three images attached they are the to be dropped into each piece, with a desciption
Updates

Project Deadline Extended
Reason: seems to be too many questions and I wasnt getting anywhere.. To clarify...One Design Piece (one page), three separate items, same peice, however three total. one for each product photo supplied

I moved the deadline back as there were many questions. To clarify, one design piece to be reused for three different products (sandwiches in this case) Same piece, but one for each sandwich.

I posted a file called Artmarket that now has each photo partnered with its title and description

Target Market(s)

hungry people looking for lunch

Industry/Entity Type

Promo

Requirements
Must have
• Attached Menu front page elements, of chalkboard, chalk font existing front colors.

```html
<!DOCTYPE html>
<html lang="en">
<head>
<meta charset="utf-8">
<title>Bistro BBQ Chicken Sandwich</title>
<link rel="stylesheet" href="https://fonts.googleapis.com/css2?family=Parisienne&family=Gochi+Hand&display=swap">
<style>
  :root {
    --chalkboard: #2a2a28;
    --chalkboard-deep: #1a1a19;
    --chalkboard-light: #363633;
    --chalk-white: #ebe8e2;
    --chalk-orange: #cf7a2e;
    --frame-white: #ffffff;
    --photo-wood: #c79a6a;
    --photo-burlap: #a88f70;
    --photo-bread: #e0b878;
    --photo-char: #4a2516;
  }
  * { box-sizing: border-box; margin: 0; padding: 0; }
  html, body {
    width: 837px;
    height: 1200px;
    overflow: hidden;
    background: var(--chalkboard-deep);
  }
  .promo-card {
    position: relative;
    width: 837px;
    height: 1200px;
    overflow: hidden;
    background:
      radial-gradient(ellipse at 50% 30%, var(--chalkboard-light) 0%, var(--chalkboard) 50%, var(--chalkboard-deep) 100%);
  }
  .chalk-texture {
    position: absolute;
    inset: 0;
    width: 837px;
    height: 1200px;
    pointer-events: none;
  }
  .dish-title {
    position: absolute;
    top: 34px;
    left: 0;
    width: 100%;
    text-align: center;
    font-family: "Parisienne", cursive;
    font-weight: 400;
    font-size: 74px;
    line-height: 112px;
    color: var(--chalk-white);
    letter-spacing: 1px;
    opacity: 0.93;
  }
  .dish-title .title-line { display: block; }
  .dish-title .title-line--first { padding-right: 20px; }
  .dish-description {
    position: absolute;
    top: 300px;
    left: 0;
    width: 100%;
    text-align: center;
    font-family: "Gochi Hand", cursive;
    font-size: 35px;
    line-height: 47.5px;
    letter-spacing: 0.3px;
    color: var(--chalk-orange);
    opacity: 0.95;
  }
  .dish-description .desc-line { display: block; white-space: nowrap; }
  .photo-frame {
    position: absolute;
    left: 33px;
    top: 542px;
    width: 773px;
    height: 630px;
    background: var(--frame-white);
    border-radius: 10px;
    padding: 11px;
  }
  .dish-photo {
    width: 100%;
    height: 100%;
    background:
      radial-gradient(ellipse at 47% 55%, var(--photo-char) 0%, #7a3a1e 18%, var(--photo-bread) 38%, transparent 60%),
      linear-gradient(180deg, var(--photo-burlap) 0%, var(--photo-burlap) 14%, var(--photo-wood) 22%, #b5824f 100%);
  }
</style>
</head>
<body>
  <main class="promo-card">
    <svg class="chalk-texture" viewBox="0 0 837 1200" aria-hidden="true">
      <defs>
        <filter id="chalk-smudge" x="0" y="0" width="100%" height="100%">
          <feTurbulence type="fractalNoise" baseFrequency="0.006 0.012" numOctaves="4" seed="7"/>
          <feColorMatrix type="matrix" values="0 0 0 0 0.85  0 0 0 0 0.85  0 0 0 0 0.82  0 0 0 0.55 -0.18"/>
        </filter>
        <filter id="chalk-dust" x="0" y="0" width="100%" height="100%">
          <feTurbulence type="fractalNoise" baseFrequency="0.85" numOctaves="2" seed="3"/>
          <feColorMatrix type="matrix" values="0 0 0 0 0.9  0 0 0 0 0.9  0 0 0 0 0.88  0 0 0 1.6 -0.95"/>
        </filter>
        <filter id="chalk-streaks" x="0" y="0" width="100%" height="100%">
          <feTurbulence type="fractalNoise" baseFrequency="0.003 0.06" numOctaves="3" seed="11"/>
          <feColorMatrix type="matrix" values="0 0 0 0 0.8  0 0 0 0 0.8  0 0 0 0 0.78  0 0 0 0.5 -0.22"/>
        </filter>
      </defs>
      <rect width="837" height="1200" filter="url(#chalk-smudge)" opacity="0.55"/>
      <rect width="837" height="1200" filter="url(#chalk-streaks)" opacity="0.35"/>
      <rect width="837" height="1200" filter="url(#chalk-dust)" opacity="0.28"/>
    </svg>
    <h1 class="dish-title">
      <span class="title-line title-line--first">Bistro BBQ</span>
      <span class="title-line">Chicken Sandwich</span>
    </h1>
    <p class="dish-description">
      <span class="desc-line">Perfectly grilled BBQ Chicken breast,</span>
      <span class="desc-line">dill yogurt dressing, Garlic spread, micro greens,</span>
      <span class="desc-line">Radish and Red bell pepper on fresh Focaccia bread</span>
    </p>
    <figure class="photo-frame">
      <div class="dish-photo" role="img" aria-label="Photo of a BBQ chicken sandwich on focaccia with micro greens, radish and red bell pepper, on a wooden board"></div>
    </figure>
  </main>
</body>
</html>
```